Harbor Rest Company Needs Business Card

Looking for a very nice looking business card. Creative but not extravagant. We sell beds and pillows across the U.S. and need something professional but catchy. I have attached the logo.

Name : Dale Morton
Title : President
Phone : (800) 417-2960
Email: rest@quiltano.com
Website: www.quiltano.com

Can be single-sided or double-sided
horizontal or vertical

Can use Blues/Greys

Target Market(s)

Mass Market

Industry/Entity Type

Retail

Contact Information for Business Card

Name : Dale Morton
Title : President
Phone : (800) 417-2960
Email: rest@quiltano.com
Website: www.quiltano.com

Requirements
Must have
• Clean, Modern, Smooth
• Can use Blues/Greys
• On the other side without the information - have something simple like www.quiltano.com or our logo
Nice to have
• Surprise me
Should not have
• Nothing crazy, nothing cluttered

```html
<!DOCTYPE html>
<html lang="en">
<head>
<meta charset="utf-8">
<title>Harbor Rest Company — Business Card</title>
<link rel="stylesheet" href="https://fonts.googleapis.com/css2?family=Ubuntu:wght@300;400;500;700&display=swap">
<style>
  :root {
    --backdrop: #d3d6da;
    --card-black: #000000;
    --card-white: #ffffff;
    --brand-blue: #2a9fd8;
    --ink: #1a1a1a;
    --url-white: #ffffff;
  }
  * { margin: 0; padding: 0; box-sizing: border-box; }
  html, body {
    width: 1200px; height: 1200px; overflow: hidden;
    background: var(--backdrop);
    font-family: "Ubuntu", sans-serif;
  }
  .canvas { position: relative; width: 1200px; height: 1200px; }

  .card {
    position: absolute; left: 120px; width: 960px; height: 549px;
    overflow: hidden;
    box-shadow: 0 10px 26px rgba(0,0,0,0.28);
  }
  .card--front { top: 34px; background: var(--card-black); }
  .card--back  { top: 617px; background: var(--card-white); }

  .accent-field {
    position: absolute;
  }
  .card--front .accent-field {
    left: 0; top: 0; width: 360px; height: 330px;
    clip-path: polygon(0 0, 100% 0, 0 100%);
    background: linear-gradient(135deg, var(--brand-blue) 0%, rgba(42,159,216,0.55) 55%, rgba(42,159,216,0) 100%);
  }
  .card--back .accent-field {
    left: 0; bottom: 0; width: 320px; height: 345px;
    clip-path: polygon(0 0, 100% 100%, 0 100%);
    background: linear-gradient(45deg, var(--brand-blue) 0%, rgba(42,159,216,0.6) 55%, rgba(42,159,216,0) 100%);
  }

  .wordmark {
    position: absolute;
    font-family: "Ubuntu", sans-serif;
    font-weight: 300;
    color: var(--brand-blue);
    line-height: 1;
    white-space: nowrap;
  }
  .card--front .wordmark {
    left: 0; right: 0; top: 222px; text-align: center;
    font-size: 168px; letter-spacing: 2px;
  }
  .card--back .wordmark {
    left: 205px; top: 78px;
    font-size: 124px; letter-spacing: 1px;
  }

  .site-url {
    position: absolute; left: 0; right: 0; top: 460px;
    text-align: center; font-weight: 700; font-size: 24px;
    letter-spacing: 9px; color: var(--url-white);
  }
  .site-url .site-url__name { color: var(--brand-blue); }

  .contact-block {
    position: absolute; left: 537px; top: 285px;
  }
  .contact-block__name {
    font-weight: 500; font-size: 29px; color: var(--ink); letter-spacing: 0.3px;
  }
  .contact-block__title {
    font-weight: 500; font-size: 29px; color: var(--brand-blue); margin-top: -2px;
  }
  .contact-list { list-style: none; margin-top: 28px; }
  .contact-list li {
    display: flex; align-items: center; gap: 12px;
    font-size: 22px; color: var(--ink); line-height: 36px;
  }
  .contact-list svg { width: 18px; height: 18px; fill: var(--brand-blue); flex: none; }
</style>
</head>
<body>
<main class="canvas">

  <section class="card card--front" aria-label="Card front">
    <div class="accent-field" role="img" aria-label="Diagonal blue streak pattern in the top-left corner"></div>
    <div class="wordmark">quiltano</div>
    <div class="site-url">www.<span class="site-url__name">quiltano</span>.com</div>
  </section>

  <section class="card card--back" aria-label="Card back with contact details">
    <div class="accent-field" role="img" aria-label="Diagonal blue streak pattern in the bottom-left corner"></div>
    <div class="wordmark">quiltano</div>
    <div class="contact-block">
      <div class="contact-block__name">DALE MORTON</div>
      <div class="contact-block__title">President</div>
      <ul class="contact-list">
        <li>
          <svg viewBox="0 0 20 20" aria-hidden="true"><path d="M2 6c0-2 3-3.5 8-3.5S18 4 18 6v1.5h-4V6H6v1.5H2z"/><path d="M5 8.5h10l2 8H3z"/><circle cx="10" cy="12.3" r="2" fill="#fff"/></svg>
          (800) 417-2960
        </li>
        <li>
          <svg viewBox="0 0 20 20" aria-hidden="true"><path d="M2 8l8-5 8 5v9H2z"/><path d="M2 8l8 5 8-5" fill="none" stroke="#fff" stroke-width="1.4"/></svg>
          rest@quiltano.com
        </li>
        <li>
          <svg viewBox="0 0 20 20" aria-hidden="true"><circle cx="10" cy="10" r="8"/><g fill="none" stroke="#fff" stroke-width="1.1"><ellipse cx="10" cy="10" rx="3.5" ry="8"/><path d="M2 10h16M3.5 6h13M3.5 14h13"/></g></svg>
          www.quiltano.com
        </li>
      </ul>
    </div>
  </section>

</main>
</body>
</html>
```